CASH PAYMENT DISCOUNT NOTICE POSTED IN CASH REGISTER AREA

LOOKING TO MAKE A FLYER OR A POSTED NOTICE FOR CUSTOMERS PAYING FOR OVER-THE-COUNTER MERCHANDISE AND WHO PAY BY CASH METHOD TO GET A 4% CASH DISCOUNT.
PRESCRIPTIONS ARE EXCLUDED FROM THIS CASH DISCOUNT.

Target Market(s)

RETAIL CUSTOMERS

Industry/Entity Type

RETAIL PHARMACY

Colors
0054AA
0677BA
7BADD7
CADEEF
E8F1F8
EB3D1F
EC4F4E
F09395
F8D3D4
FCEDEE

Requirements
Must have
• LOGO COLORS
Nice to have
• EYE CATCHING

```html
<!DOCTYPE html>
<html lang="en">
<head>
<meta charset="utf-8">
<title>Cash Discount Notice</title>
<link rel="stylesheet" href="https://fonts.googleapis.com/css2?family=Roboto:wght@700;900&display=swap">
<style>
  :root {
    --blue-deep: #0054AA;
    --blue-mid: #0677BA;
    --blue-soft: #7BADD7;
    --blue-pale: #CADEEF;
    --blue-mist: #E8F1F8;
    --red: #EB3D1F;
    --red-warm: #EC4F4E;
    --red-dark: #C9261A;
    --pink: #F09395;
    --pink-pale: #F8D3D4;
    --white: #FFFFFF;
  }
  * { margin: 0; padding: 0; box-sizing: border-box; }
  html, body {
    width: 1200px;
    height: 674px;
    overflow: hidden;
    background: var(--blue-mist);
    font-family: "Roboto", Arial, sans-serif;
  }
  .stage {
    width: 1200px;
    height: 674px;
    display: flex;
    align-items: center;
    justify-content: center;
  }
  .notice {
    position: relative;
    width: 410px;
    height: 620px;
    background: linear-gradient(180deg, var(--red-warm) 0%, var(--red) 45%, var(--red-dark) 100%);
    overflow: hidden;
    box-shadow: 0 6px 24px rgba(0, 84, 170, 0.18);
  }
  .notice__pointer {
    position: absolute;
    top: 0;
    left: 0;
    width: 410px;
    height: 110px;
  }
  .notice__here {
    position: absolute;
    top: 22px;
    left: 0;
    width: 100%;
    text-align: center;
    color: var(--red);
    font-weight: 900;
    font-size: 38px;
    letter-spacing: 1px;
    line-height: 1;
  }
  .notice__lead {
    position: absolute;
    top: 132px;
    left: 0;
    width: 100%;
    text-align: center;
    color: var(--white);
    font-weight: 900;
    font-size: 38px;
    line-height: 1.1;
    letter-spacing: 0.5px;
  }
  .notice__rate {
    position: absolute;
    top: 222px;
    left: 0;
    width: 100%;
    text-align: center;
    color: var(--white);
    font-weight: 900;
    font-size: 172px;
    line-height: 1;
    letter-spacing: -4px;
  }
  .notice__label {
    position: absolute;
    top: 400px;
    left: 0;
    width: 100%;
    text-align: center;
    color: var(--white);
    font-weight: 900;
    font-size: 48px;
    line-height: 1;
    letter-spacing: 1px;
  }
  .notice__terms {
    position: absolute;
    top: 460px;
    left: 0;
    width: 100%;
    text-align: center;
    color: var(--pink-pale);
    font-weight: 700;
    font-size: 16px;
    line-height: 1;
    letter-spacing: 0.5px;
  }
  .notice__footer {
    position: absolute;
    left: 0;
    bottom: 0;
    width: 410px;
    height: 150px;
  }
  .brand {
    position: absolute;
    bottom: 30px;
    right: 36px;
    display: flex;
    align-items: center;
    gap: 10px;
    color: var(--blue-deep);
    font-weight: 700;
    font-size: 24px;
    line-height: 1;
  }
  .brand__mark {
    width: 18px;
    height: 18px;
    background: var(--blue-deep);
  }
</style>
</head>
<body>
  <main class="stage">
    <section class="notice" aria-label="Cash payment discount notice">
      <svg class="notice__pointer" viewBox="0 0 410 110" aria-hidden="true">
        <path d="M40 12 H370 V70 H240 L205 100 L170 70 H40 Z" fill="var(--white)"/>
      </svg>
      <div class="notice__here">HERE</div>
      <h1 class="notice__lead">PAY CASH<br>AND RECEIVE</h1>
      <div class="notice__rate">4%</div>
      <div class="notice__label">DISCOUNT</div>
      <p class="notice__terms">PRESCRIPTIONS EXCLUDED</p>
      <svg class="notice__footer" viewBox="0 0 410 150" aria-hidden="true">
        <path d="M0 62 Q200 30 410 20 V34 Q200 44 0 78 Z" fill="var(--blue-mid)"/>
        <path d="M0 78 Q200 44 410 34 V150 H0 Z" fill="var(--white)"/>
      </svg>
      <div class="brand">
        <span class="brand__mark"></span>
        <span class="brand__name">Northvale Pharmacy</span>
      </div>
    </section>
  </main>
</body>
</html>
```